NEW YORK Plumbing/utility company 10 year anniversary business card

Looking For simple back and front business card would like to include a few things in description
We offer 24/7 emergency service
residential
commercial
industrial
municipal
services offered
Plumbing
hydro excavation
hydro jetting
Well pumps
Sewer pumps
water mains
sewer mains

```html
<!DOCTYPE html>
<html lang="en">
<head>
<meta charset="utf-8">
<title>Ridgeline Water &amp; Sewer – Business Card</title>
<link href="https://fonts.googleapis.com/css2?family=Montserrat:wght@400;500;600;700;800&display=swap" rel="stylesheet">
<style>
  :root {
    --brand-blue: #0b5fa5;
    --deep-blue: #0a4f8c;
    --pattern-blue: #1c6bb0;
    --alert-red: #e42229;
    --ink: #3b3b3b;
    --paper: #ffffff;
    --backdrop: #2a2a2c;
  }
  * { box-sizing: border-box; margin: 0; padding: 0; }
  html, body {
    width: 1200px; height: 900px; overflow: hidden;
    background: var(--backdrop);
    font-family: "Montserrat", sans-serif;
  }
  .sheet {
    width: 1200px; height: 900px;
    display: flex; flex-direction: column; align-items: center; justify-content: center;
    gap: 50px;
  }
  .card {
    width: 630px; height: 360px;
    border-radius: 22px; overflow: hidden; position: relative;
    box-shadow: 0 10px 30px rgba(0,0,0,.45);
  }
  /* Front */
  .card-front { background: var(--paper); display: flex; flex-direction: column; }
  .front-body {
    flex: 1; display: flex; flex-direction: column; align-items: center;
    padding-top: 34px; text-align: center;
  }
  .brand-name {
    font-weight: 800; font-size: 30px; letter-spacing: 1px;
    color: var(--brand-blue); text-transform: uppercase; line-height: 1.1;
  }
  .brand-name .mark {
    display: inline-block; width: 22px; height: 22px; border-radius: 50%;
    background: var(--brand-blue); vertical-align: -2px; margin-right: 10px;
  }
  .emergency {
    margin-top: 18px; font-weight: 700; font-size: 21px;
    color: var(--alert-red); text-transform: uppercase; letter-spacing: .3px;
  }
  .sectors { margin-top: 6px; font-size: 15px; color: var(--ink); font-weight: 500; }
  .services-title {
    margin-top: 12px; font-weight: 700; font-size: 16px;
    color: var(--brand-blue); text-transform: uppercase;
  }
  .services { margin-top: 4px; font-size: 15px; color: var(--ink); line-height: 1.45; font-weight: 500; }
  .dot-blue { color: var(--brand-blue); }
  .dot-red { color: var(--alert-red); }
  .contact-band {
    height: 72px; background: var(--brand-blue);
    display: flex; align-items: center; justify-content: center; gap: 60px;
    color: var(--paper); font-size: 17px; font-weight: 500; letter-spacing: .3px;
  }
  .contact-item { display: flex; align-items: center; gap: 10px; }
  .contact-item svg { width: 18px; height: 18px; fill: var(--paper); }
  /* Back */
  .card-back { background: var(--brand-blue); }
  .back-pattern {
    position: absolute; inset: 0;
    background: linear-gradient(135deg, var(--deep-blue), var(--pattern-blue) 50%, var(--brand-blue));
  }
  .back-name {
    position: absolute; right: 40px; bottom: 48px;
    font-weight: 800; font-size: 34px; letter-spacing: 1px; color: var(--paper);
  }
</style>
</head>
<body>
<main class="sheet">
  <section class="card card-front">
    <div class="front-body">
      <h1 class="brand-name"><span class="mark"></span>Ridgeline Water &amp; Sewer</h1>
      <p class="emergency">We offer 24/7 emergency service</p>
      <p class="sectors">Residential <span class="dot-blue">•</span> Commercial <span class="dot-blue">•</span> Industrial <span class="dot-blue">•</span> Municipal</p>
      <h2 class="services-title">Services offered</h2>
      <p class="services">
        Plumbing <span class="dot-red">•</span> hydro excavation <span class="dot-red">•</span> hydro jetting <span class="dot-red">•</span> Well pumps<br>
        Sewer pumps <span class="dot-red">•</span> water mains <span class="dot-red">•</span> sewer mains
      </p>
    </div>
    <footer class="contact-band">
      <span class="contact-item">
        <svg viewBox="0 0 24 24" aria-hidden="true"><path d="M6.6 10.8a15.1 15.1 0 0 0 6.6 6.6l2.2-2.2a1 1 0 0 1 1-.25 11.4 11.4 0 0 0 3.6.57 1 1 0 0 1 1 1V20a1 1 0 0 1-1 1A17 17 0 0 1 3 4a1 1 0 0 1 1-1h3.5a1 1 0 0 1 1 1c0 1.25.2 2.45.57 3.57a1 1 0 0 1-.25 1z"/></svg>
        555-014-2271
      </span>
      <span class="contact-item">
        <svg viewBox="0 0 24 24" aria-hidden="true"><path d="M3 5h18v14H3z M3 5l9 7 9-7" fill="none" stroke="#fff" stroke-width="2"/></svg>
        info@ridgelinews.com
      </span>
    </footer>
  </section>

  <section class="card card-back">
    <div class="back-pattern" role="img" aria-label="Repeating tone-on-tone brand pattern in shades of blue"></div>
    <p class="back-name">RWS</p>
  </section>
</main>
</body>
</html>
```